Website Design for Marvane Equity Partners

I am looking to create a website with 3-4 pages for Marvane Equity Partners, a private investment holding company. We already have a logo created via PixelHarbor and would like to incorporate the same dark navy blue color scheme as well as white and potentially other colors including variants of blue, black, and white. We are looking for a conservative, polished design befitting a financial services firm. Our focus as a firm is on identifying opportunities in the overlooked - seeing opportunity where institutional investment is lacking. We are focused on building value for the long-term. We will provide virtually all of the text content but need assistance in setting up the layout, font, design, theme, graphics, etc. The initial three pages will be: Home Page / About Us, "Team", and "Portfolio". Right now, we do not have any portfolio companies but will likely have one within the next several months. The main content page will be the home page. The Team and Portfolio pages will be abbreviated. This website will be expository and is not primarily focused on lead generation or sales.

Ideally, we can incorporate some form of animations / transitions for titles and text sections and stock images (or ideally looped videos) of major city skylines in the U.S. , Latin America, and Europe as those regions are our core investment geographies.

Websites we like that you can use for references include many major private equity firms including Quarrystone Equity (https://www.quarrystoneequity.example/), Briarvale (https://briarvale.example/), KRU Holdings (https://www.kruholdings.example/), and Halvorwick (https://www.halvorwick.example/)
Updates

All,

Thank you to everyone who has posted the initial drafts of the Marvane Equity Partners website. The designs are very good. We would now like to review more refined drafts of our website from the designers.

We have posted updated, specific guidance on website page design and text. Please reference the new uploaded "Marvane Equity Partners Website Design Guidance" Microsoft Word document to refine your submissions.

Thank you!
Ferdinand

Target Market(s)

Investment Professionals

Industry/Entity Type

Financial Services

Coding

Coded - Design and coding required

Number of Pages Required

4 page

```html
<!DOCTYPE html>
<html lang="en">
<head>
<meta charset="utf-8">
<title>Marvane Equity Partners</title>
<link rel="stylesheet" href="https://fonts.googleapis.com/css2?family=Outfit:wght@300;400;500;600&display=swap">
<style>
:root{
  --navy:#0f1e3a;
  --navy-2:#1a2a48;
  --accent:#4a6a97;
  --accent-soft:#6d86ad;
  --sand:#f6f3ef;
  --ink:#1a1f2b;
  --muted:#5b6170;
  --line:#c9ccd3;
  --white:#ffffff;
}
*{box-sizing:border-box;margin:0;padding:0}
html,body{width:1200px;height:4236px;overflow:hidden}
body{position:relative;background:var(--white);font-family:'Outfit',sans-serif;color:var(--ink)}
.abs{position:absolute}
.brand{font-weight:600;letter-spacing:4px;color:var(--navy);font-size:34px}
.nav a{position:absolute;top:35px;font-size:13px;color:var(--muted);text-decoration:none;letter-spacing:.5px}
.nav a.active{color:var(--navy);border-bottom:1px solid var(--navy);padding-bottom:3px}
.pill{position:absolute;display:flex;align-items:center;border:1px solid var(--navy);border-radius:30px;background:var(--white);overflow:hidden}
.pill span{flex:1;text-align:center;font-size:13px;color:var(--navy);letter-spacing:.4px}
.pill i{width:38px;height:100%;background:var(--navy);border-radius:30px;display:flex;align-items:center;justify-content:center}
.pill i svg{width:12px;height:12px}
.hero-card{left:120px;top:118px;width:393px;height:252px;background:rgba(255,255,255,.95);border-radius:22px;padding:40px 38px}
.hero-card h1{font-weight:500;font-size:21px;line-height:43px;color:var(--navy)}
.hl{color:var(--accent)}
.trust{top:670px;left:105px;width:990px;display:flex;align-items:center;gap:22px}
.trust hr{flex:1;border:none;border-top:1px solid var(--line)}
.trust p{font-size:17px;font-weight:500;color:var(--navy)}
.partner{top:724px;display:flex;align-items:center;gap:10px;font-size:36px;font-weight:600;color:var(--ink)}
.partner b{width:30px;height:30px;background:var(--accent);border-radius:50%;display:block}
.section-title{font-weight:500;font-size:29px;color:var(--navy);display:flex;align-items:center;gap:16px}
.section-title::after{content:"";width:36px;border-top:2px solid var(--navy)}
.about-text{left:653px;top:870px;width:450px}
.about-text h3{font-weight:500;font-size:15px;line-height:38px;color:var(--navy);margin-top:14px}
.about-text p{font-size:14.5px;line-height:38px;color:var(--muted);margin-top:12px;font-weight:300}
.insights{left:110px;top:1489px;width:1090px;height:298px;background:var(--navy);border-radius:150px 0 0 150px}
.insights .section-title{color:var(--white);position:absolute;left:97px;top:58px}
.insights .section-title::after{border-color:var(--white)}
.stat{position:absolute;top:140px;display:flex;gap:16px}
.stat svg{width:56px;height:56px;margin-top:8px}
.stat strong{display:block;font-size:33px;font-weight:500;color:var(--white)}
.stat small{display:block;font-size:13px;color:var(--accent-soft);margin-top:10px;letter-spacing:.4px}
.sand{left:0;top:1637px;width:1200px;height:688px;background:var(--sand)}
.services-intro{left:542px;top:1862px;width:560px;font-size:14.5px;line-height:36px;color:var(--ink);font-weight:300}
.card{top:1966px;width:307px;height:286px;background:var(--white);border:1px solid #e2e2e6;border-radius:18px;padding:13px}
.card.active{background:var(--navy);border-color:var(--navy)}
.card .ph{height:203px;border-radius:12px}
.card .lbl{display:flex;justify-content:space-between;align-items:center;padding:28px 16px 0 16px;font-size:15.5px;font-weight:500;color:var(--navy)}
.card.active .lbl{color:var(--white)}
.approach-title{top:2398px;left:0;width:1200px;display:flex;justify-content:center;align-items:center;gap:22px;font-size:29px;font-weight:500;color:var(--navy)}
.approach-title::before,.approach-title::after{content:"";width:36px;border-top:2px solid var(--navy)}
.step{top:2484px;width:330px;text-align:center}
.step .dot{width:132px;height:132px;border-radius:50%;background:var(--navy);margin:0 auto;position:relative;display:flex;align-items:center;justify-content:center}
.step .dot.lit{background:var(--accent)}
.step .num{position:absolute;left:88px;top:81px;width:50px;height:50px;border-radius:50%;background:var(--white);border:1px solid #dfe2e8;display:flex;align-items:center;justify-content:center;font-size:19px;color:var(--navy)}
.step .num.lit{color:var(--accent)}
.step h4{margin-top:38px;font-size:17px;font-weight:500;line-height:38px;color:var(--navy)}
.step h4.lit{color:var(--accent)}
.step p{margin-top:4px;font-size:14px;line-height:34px;color:var(--muted);font-weight:300}
.community-title{top:2990px;left:0;width:1200px;text-align:center;color:var(--white);font-size:29px;font-weight:500}
.community-sub{top:3050px;left:0;width:1200px;display:flex;justify-content:center;align-items:center;gap:22px;font-size:29px;font-weight:500;color:var(--accent-soft)}
.community-sub::before,.community-sub::after{content:"";width:36px;border-top:2px solid var(--white)}
.avatar{position:absolute;border-radius:50%;border:3px solid var(--white);background:linear-gradient(160deg,#c8b8a8,#7c8ca3)}
.quote{width:288px;background:var(--navy-2);border-radius:22px;text-align:center;color:var(--white);padding:26px 12px}
.quote .stars{color:#f4c430;font-size:20px;letter-spacing:6px}
.quote p{font-size:14.5px;line-height:36px;font-weight:300;margin-top:10px}
.quote cite{display:block;font-style:normal;font-size:13px;font-weight:500;margin-top:12px;letter-spacing:.3px}
.footer-bg{left:0;top:3676px;width:1200px;height:560px;background:var(--sand)}
.cta{left:112px;top:3738px;font-size:22px;font-weight:500;color:var(--navy)}
.email{left:718px;top:3734px;width:370px;height:39px;border:1px solid var(--navy);border-radius:30px;display:flex;align-items:center;overflow:hidden;background:var(--white)}
.email span{flex:1;padding-left:16px;font-size:12.5px;color:var(--muted);letter-spacing:.4px}
.email i{width:42px;height:100%;background:var(--navy);border-radius:30px;display:flex;align-items:center;justify-content:center}
.rule{left:110px;width:978px;border-top:1px solid #a9adb6}
.col{top:3864px}
.col h5{font-size:18px;font-weight:500;color:var(--accent);padding-bottom:10px;position:relative}
.col h5::after{content:"";position:absolute;left:0;bottom:0;width:34px;border-top:2px solid var(--accent)}
.col ul{list-style:none;margin-top:18px}
.col li{font-size:12.5px;color:var(--ink);line-height:36.5px;letter-spacing:.3px}
.copyright{right:112px;top:4183px;font-size:13px;color:var(--navy);letter-spacing:.3px}
</style>
</head>
<body>

<header>
  <div class="abs brand" style="left:112px;top:24px">MARVANE</div>
  <nav class="nav">
    <a class="active" style="left:654px">HOME</a>
    <a style="left:741px">TEAM</a>
    <a style="left:814px">PORTFOLIO</a>
  </nav>
  <div class="pill" style="left:950px;top:28px;width:138px;height:33px"><span>CONTACT US</span><i><svg viewBox="0 0 12 12"><path d="M4 2l4 4-4 4" fill="none" stroke="#fff" stroke-width="1.6"/></svg></i></div>
</header>

<section class="hero">
  <svg class="abs" style="left:87px;top:82px" width="1026" height="518" viewBox="0 0 1026 518" role="img" aria-label="City skyline at dusk with glass towers and a spiralling tower">
    <defs><linearGradient id="dusk" x1="0" y1="0" x2="0" y2="1"><stop offset="0" stop-color="#7a93b8"/><stop offset=".4" stop-color="#c9a98a"/><stop offset=".7" stop-color="#3b4a5e"/><stop offset="1" stop-color="#1d2a38"/></linearGradient></defs>
    <path d="M26 0H1000Q1026 0 1026 26V468Q1026 518 976 518H520Q490 518 470 495L440 445Q425 421 395 421H40Q0 421 0 381V26Q0 0 26 0Z" fill="url(#dusk)"/>
  </svg>
  <div class="abs hero-card">
    <h1>INVESTING IN THE<br>OVERLOOKED. <span class="hl">BUILDING FOR<br>THE LONG TERM</span></h1>
  </div>
  <div class="pill" style="left:158px;top:298px;width:166px;height:39px"><span>INVEST NOW</span><i style="width:42px"><svg viewBox="0 0 12 12"><path d="M4 2l4 4-4 4" fill="none" stroke="#fff" stroke-width="1.6"/></svg></i></div>
</section>

<section class="partners">
  <div class="abs trust"><hr><p>1K+ BRANDS TRUST US</p><hr></div>
  <div class="abs partner" style="left:112px"><b></b>Kestrel</div>
  <div class="abs partner" style="left:388px"><b></b>Kestrel</div>
  <div class="abs partner" style="left:664px"><b></b>Kestrel</div>
  <div class="abs partner" style="left:940px"><b></b>Kestrel</div>
</section>

<section class="about">
  <div class="abs" style="left:110px;top:850px;width:464px;height:556px;background:var(--navy);border-radius:24px"></div>
  <div class="abs" role="img" aria-label="Two businesswomen in conversation at a meeting table" style="left:122px;top:850px;width:452px;height:544px;border-radius:24px;background:linear-gradient(135deg,#e8e2d8,#b9a690 55%,#7d6a58)"></div>
  <div class="abs about-text">
    <div class="section-title">ABOUT&nbsp;<span class="hl" style="margin-left:-10px">MARVANE</span></div>
    <h3>UNLOCK THE RIGHT STRATEGIES, SUPPORT,<br>AND EXPERTISE</h3>
    <p>Marvane Equity Partners is a private investment holding company focused on long-term value creation in overlooked and undercapitalized sectors.</p>
    <p>Founded on the belief that opportunity often exists where others aren’t looking, we invest in businesses that stand to benefit from strategic guidance, patient capital, and operational rigor.</p>
  </div>
  <div class="pill" style="left:654px;top:1333px;width:165px;height:38px"><span>LEARN MORE</span><i style="width:42px"><svg viewBox="0 0 12 12"><path d="M4 2l4 4-4 4" fill="none" stroke="#fff" stroke-width="1.6"/></svg></i></div>
</section>

<div class="abs sand"></div>

<section class="abs insights">
  <div class="section-title">COMPANY&nbsp;<span class="hl" style="margin-left:-10px;color:var(--accent-soft)">INSIGHTS</span></div>
  <div class="stat" style="left:88px">
    <svg viewBox="0 0 56 56" fill="none" stroke="#fff" stroke-width="1.6"><rect x="8" y="10" width="34" height="26" rx="2"/><path d="M14 30l7-8 6 5 9-11"/><circle cx="42" cy="40" r="8"/><path d="M42 36v8M39 40h6"/></svg>
    <div><strong>$49BN</strong><small>ASSETS UNDER MANAGEMENT</small></div>
  </div>
  <div class="stat" style="left:500px">
    <svg viewBox="0 0 56 56" fill="none" stroke="#fff" stroke-width="1.6"><circle cx="28" cy="16" r="6"/><path d="M18 34a10 10 0 0 1 20 0"/><circle cx="12" cy="40" r="4"/><circle cx="44" cy="40" r="4"/><path d="M5 52a7 7 0 0 1 14 0M37 52a7 7 0 0 1 14 0"/></svg>
    <div><strong>160+</strong><small>GLOBAL STAFF</small></div>
  </div>
  <div class="stat" style="left:796px">
    <svg viewBox="0 0 56 56" fill="none" stroke="#fff" stroke-width="1.6"><circle cx="28" cy="28" r="20"/><ellipse cx="28" cy="28" rx="9" ry="20"/><path d="M8 28h40M12 18h32M12 38h32"/></svg>
    <div><strong>60+</strong><small>WORLDWIDE FOOTPRINT</small></div>
  </div>
</section>

<section class="services">
  <div class="abs section-title" style="left:112px;top:1862px">MARVANE&nbsp;<span class="hl" style="margin-left:-10px">SERVICES</span></div>
  <p class="abs services-intro">At Marvane Equity Partners, we don’t just provide capital — we bring long term partnership, operational insight, and strategic clarity.</p>
  <div class="abs card" style="left:112px"><div class="ph" role="img" aria-label="Hands with a calculator over financial reports" style="background:linear-gradient(135deg,#d9dce2,#8e97a6)"></div><div class="lbl">STRATEGIC CAPITAL<span>⟶</span></div></div>
  <div class="abs card active" style="left:446px"><div class="ph" role="img" aria-label="Team discussing work around a meeting table" style="background:linear-gradient(135deg,#d8cfc3,#8a7c6c)"></div><div class="lbl">OPERATIONAL SUPPORT<span>⟶</span></div></div>
  <div class="abs card" style="left:781px"><div class="ph" role="img" aria-label="Business handshake over a signed contract" style="background:linear-gradient(135deg,#b8a48e,#4d3e32)"></div><div class="lbl">GOVERNANCE &amp; ALIGNMENT<span>⟶</span></div></div>
</section>

<section class="approach">
  <div class="abs approach-title">THE MARVANE <span class="hl" style="margin-left:-14px">APPROACH</span></div>
  <svg class="abs" style="left:345px;top:2548px" width="520" height="4"><path d="M0 2H140M380 2H520" stroke="#c9ccd3" stroke-dasharray="4 4"/></svg>
  <div class="abs step" style="left:65px">
    <div class="dot"><svg width="52" height="52" viewBox="0 0 52 52" fill="none" stroke="#fff" stroke-width="1.6"><rect x="10" y="6" width="26" height="36" rx="2"/><path d="M16 14h14M16 22h14M16 30h8"/><circle cx="36" cy="36" r="7"/><path d="M41 41l6 6"/></svg><div class="num">01</div></div>
    <h4>DISCOVER WHAT OTHERS<br>MISS</h4>
    <p>We source investment opportunities in undercapitalized sectors and overlooked geographies</p>
  </div>
  <div class="abs step" style="left:438px">
    <div class="dot lit"><svg width="52" height="52" viewBox="0 0 52 52" fill="none" stroke="#fff" stroke-width="1.6"><path d="M8 44V34M16 44V28M24 44V30M32 44V22M40 44V14"/><path d="M8 26l10-8 8 4 16-14M36 8h6v6"/></svg><div class="num lit">02</div></div>
    <h4 class="lit">INVEST WITH CONVICTION</h4>
    <p>Our capital is patient and strategic. With no fund expiration pressure, we invest for the long term, aligning with founders and management</p>
  </div>
  <div class="abs step" style="left:802px">
    <div class="dot"><svg width="52" height="52" viewBox="0 0 52 52" fill="none" stroke="#fff" stroke-width="1.6"><rect x="12" y="6" width="28" height="24" rx="2"/><path d="M12 18h28M26 6v24"/><circle cx="16" cy="38" r="4"/><circle cx="36" cy="38" r="4"/><path d="M8 48a8 8 0 0 1 16 0M28 48a8 8 0 0 1 16 0"/></svg><div class="num">03</div></div>
    <h4>BUILD FOR THE LONG TERM</h4>
    <p>We bring more than capital. We provide operational support, governance alignment, and strategic insight to help businesses scale sustainably</p>
  </div>
</section>

<section class="community">
  <svg class="abs" style="left:0;top:2905px" width="1200" height="771" viewBox="0 0 1200 771"><path d="M0 108Q600 -108 1200 108V771H0Z" fill="var(--navy)"/></svg>
  <div class="abs community-title">JOIN OUR GROWING COMMUNITY OF</div>
  <div class="abs community-sub">INTERNATIONAL INVESTORS</div>
  <div class="avatar" role="img" aria-label="Investor portrait" style="left:109px;top:3037px;width:60px;height:60px"></div>
  <div class="avatar" role="img" aria-label="Investor portrait" style="left:240px;top:3113px;width:70px;height:70px"></div>
  <div class="avatar" role="img" aria-label="Investor portrait" style="left:371px;top:3136px;width:56px;height:56px"></div>
  <div class="avatar" role="img" aria-label="Investor portrait" style="left:539px;top:3147px;width:122px;height:122px"></div>
  <div class="avatar" role="img" aria-label="Investor portrait" style="left:164px;top:3252px;width:56px;height:56px"></div>
  <div class="avatar" role="img" aria-label="Investor portrait" style="left:794px;top:3166px;width:56px;height:56px"></div>
  <div class="avatar" role="img" aria-label="Investor portrait" style="left:899px;top:3096px;width:34px;height:34px"></div>
  <div class="avatar" role="img" aria-label="Investor portrait" style="left:995px;top:3043px;width:70px;height:70px"></div>
  <div class="avatar" role="img" aria-label="Investor portrait" style="left:1027px;top:3209px;width:70px;height:70px"></div>

  <div class="abs quote" style="left:123px;top:3367px;height:228px">
    <div class="stars">★★★★★</div>
    <p>“Marvane wasn’t just capital — they were a catalyst. We scaled faster and smarter with their help.”</p>
    <cite>MID-MARKET LOGISTICS FIRM, BRAZIL</cite>
  </div>
  <div class="abs quote" style="left:455px;top:3318px;height:244px">
    <div class="stars">★★★★★</div>
    <p>“Their conviction in underinvested spaces is unmatched. Marvane took the long view when no one else did.”</p>
    <cite>TECH INFRASTRUCTURE COMPANY, SPAIN</cite>
  </div>
  <div class="abs quote" style="left:789px;top:3367px;height:228px">
    <div class="stars">★★★★★</div>
    <p>“They’re not just investors. They’re strategic thinkers who actually listen.”</p>
    <cite>FAMILY-OWNED BUSINESS, U.S</cite>
  </div>
</section>

<footer>
  <div class="abs footer-bg"></div>
  <div class="abs cta">LET’S START <span class="hl">INVESTING NOW</span></div>
  <div class="abs email"><span>ENTER EMAIL ADDRESS</span><i><svg width="12" height="12" viewBox="0 0 12 12"><path d="M4 2l4 4-4 4" fill="none" stroke="#fff" stroke-width="1.6"/></svg></i></div>
  <div class="abs rule" style="top:3819px"></div>
  <div class="abs col" style="left:110px"><h5>PRODUCT</h5><ul><li>FEATURES</li><li>PRICING</li><li>CREATE A FREE ACCOUNT</li><li>PRIVACY POLICY &amp; GDPR</li><li>TERMS OF SERVICE</li></ul></div>
  <div class="abs col" style="left:427px"><h5>SUPPORT</h5><ul><li>SUPPORT</li><li>KNOWLEDGE BASE</li><li>WEBINARS</li><li>API DOCUMENTATION</li><li>LOG IN</li></ul></div>
  <div class="abs col" style="left:710px"><h5>COMPANY</h5><ul><li>ABOUT US</li><li>CAREERS</li><li>LEADERSHIP</li><li>ARTICLE &amp; NEWS</li><li>LEGAL NOTICE</li></ul></div>
  <div class="abs col" style="left:967px"><h5>RESOURCES</h5><ul><li>API REFERENCE</li><li>STATUS</li><li>GET HELP</li><li>BRAND ASSETS</li><li>FINTECH SERVICES</li></ul></div>
  <div class="abs rule" style="top:4146px"></div>
  <div class="abs brand" style="left:112px;top:4170px">MARVANE</div>
  <div class="abs copyright">COPYRIGHT 2025 MARVANE. ALL RIGHTS RESERVED</div>
</footer>

</body>
</html>
```